Business Card Design

Copperfield Lantern & Spark, Inc. (CLS), located in Memphis, TN began operating on 2003. We are a certified
minority woman-owned business that genuinely takes a vested interest in our customers. We serve utilities,
government, contractors and end user markets in electrical, water, gas and industrial supplies. Our core
competency as a distributor of electrical materials has positioned us to serve business of all size. As your supply
chain partner, we arm you with the resources you need to make your supply chain more efficient. Our team
works with your team on a daily basis to help you solve problems and achieve goals. This team approach has
helped CLS customers to succeed and we can do the same for you.

NAICS Codes:
423610 Electrical Apparatus and Equipment, Wiring Supplies, and Related Equipment Merchant
Wholesalers
423510 Metal Service Centers and Other Metal Merchant Wholesalers
423720 Plumbing and Heating Equipment and Supplies (Hydronics) Merchant Wholesalers

Certifications
MBE (KRVPQAL, State of Tennessee Up-MRX and FJW), WBE (HQOLT),
WOSB, DOT (TDOT, MDOT, ALDOT, SCDOT, NCDOT, and VDOT), LOSB,
SBE, and LSB Certified
Some of Our Products Include:
. Boxes & Covers
. Conduit & Raceway
. Fittings
. Fuses
. Lamp & Ballasts
. Lighting Controls & Timers
. Lighting Fixtures
. Personal Safety
. Pipes
. Power Distribution
. Terminations Ground & Splices
. Tools & Testers
. Wire, Cords & Cable
. Wiring Devices
. Valves

Industry/Entity Type

Business

Contact Information for Business Card

Marianne T. Holloway - President/CEO
4728 Quillon Ave., Memphis, TN 38127
901-555-0147 office, 901-555-0182 fax, 901-555-0163 cell
mtholloway@clsllc-example.com - www.clsincorp-example.com

```html
<!DOCTYPE html>
<html lang="en">
<head>
<meta charset="utf-8">
<title>Copperfield Lantern &amp; Spark – Business Card</title>
<link rel="stylesheet" href="https://fonts.googleapis.com/css2?family=Cormorant+Garamond:ital,wght@0,500;0,600;1,500&display=swap">
<style>
  :root {
    --stage: #d9d9d9;
    --paper: #ffffff;
    --olive: #797c44;
    --ink: #111111;
    --night: #050505;
    --night-logo: #3d3d3d;
    --night-text: #8c8c8c;
    --mark: #8a9a3a;
    --card-w: 640px;
    --card-h: 366px;
  }
  * { box-sizing: border-box; margin: 0; padding: 0; }
  html, body { width: 1200px; height: 926px; overflow: hidden; }
  body {
    background: var(--stage);
    font-family: "Cormorant Garamond", Georgia, serif;
    position: relative;
  }
  .card {
    position: absolute;
    width: var(--card-w);
    height: var(--card-h);
    overflow: hidden;
    box-shadow: 0 6px 18px rgba(0,0,0,.25);
  }

  /* Front */
  .card--front { left: 280px; top: 60px; background: var(--paper); }
  .front__top { height: 40%; display: flex; align-items: center; justify-content: center; padding-left: 80px; }
  .brand { display: flex; align-items: center; gap: 12px; color: var(--ink); }
  .brand__dot { width: 14px; height: 14px; background: var(--mark); }
  .brand__name { font-size: 30px; font-weight: 600; letter-spacing: 1px; text-transform: uppercase; line-height: 1; }
  .front__band {
    height: 60%; background: var(--olive); color: var(--ink);
    position: relative; padding: 22px 30px;
  }
  .holder { font-size: 19px; font-weight: 500; }
  .holder__title { font-style: italic; }
  .address { margin-top: 12px; font-size: 15px; line-height: 1.3; }
  .phones {
    position: absolute; right: 30px; bottom: 62px;
    font-size: 15px; line-height: 1.35;
  }
  .phones b { font-weight: 600; }

  /* Back */
  .card--back { left: 280px; top: 500px; background: var(--night); }
  .back__body { height: 84%; display: flex; flex-direction: column; align-items: center; padding-top: 42px; }
  .back__brand { display: flex; align-items: center; gap: 12px; color: var(--night-logo); }
  .back__brand .brand__dot { background: var(--mark); }
  .back__brand .brand__name { font-size: 30px; }
  .products {
    margin-top: 30px; text-align: center; color: var(--night-text);
    font-size: 16px; line-height: 1.45; letter-spacing: .5px; text-transform: uppercase;
  }
  .back__band { height: 16%; background: var(--olive); }
</style>
</head>
<body>
  <section class="card card--front" aria-label="Business card front">
    <div class="front__top">
      <div class="brand">
        <span class="brand__dot"></span>
        <span class="brand__name">Copperfield Lantern &amp; Spark</span>
      </div>
    </div>
    <div class="front__band">
      <p class="holder">Marianne T. Holloway - <span class="holder__title">President/CEO</span></p>
      <p class="address">4728 Quillon Ave., Memphis, TN 38127<br>mtholloway@clsllc-example.com<br>www.clsincorp-example.com</p>
      <p class="phones">
        <b>cell.</b> 901-555-0147 (office)<br>
        <b>fax.</b> 901-555-0182<br>
        <b>cell.</b> 901-555-0163 (personal)
      </p>
    </div>
  </section>

  <section class="card card--back" aria-label="Business card back">
    <div class="back__body">
      <div class="brand back__brand">
        <span class="brand__dot"></span>
        <span class="brand__name">Copperfield Lantern &amp; Spark</span>
      </div>
      <p class="products">
        Boxes &amp; Covers - Conduit &amp; Raceway - Fittings<br>
        Fuses - Lamp &amp; Ballasts - Lighting Controls &amp; Timers<br>
        Lighting Fixtures - Personal Safety - Pipes - Power Distribution<br>
        Terminations Ground &amp; Splices - Tools &amp; Testers<br>
        Wire, Cords &amp; Cable - Wiring Devices - Valves
      </p>
    </div>
    <div class="back__band"></div>
  </section>
</body>
</html>
```